Brackenford Lane Vineyard website

I need to have our website design done. It is an existing site www.brackenfordlane.com.au which is based on Wordpress which includes information and online purchasing of our wine. Logo and existing branding are to be maintained but website needs to be improved and open to recommendations for function extensions.

Target Market(s)

Wine drinkers and people wanting to visit or hold and event.
Aged from 25-55, men and women

Industry/Entity Type

Vineyard

Number of Pages Required

5+ page

Font styles to use
Sans Serif

Requirements
Must have
• Incorporate existing logos and styling from bottles.
• See existing website www.brackenfordlane.com.au

```html
<!DOCTYPE html>
<html lang="en">
<head>
<meta charset="utf-8">
<title>Brackenford Lane Vineyard</title>
<link href="https://fonts.googleapis.com/css2?family=Open+Sans:wght@400;600;700&family=Tinos:wght@400;700&display=swap" rel="stylesheet">
<style>
:root{
  --green:#7a9a01;
  --green-dark:#5f7a00;
  --black:#000;
  --ink:#1a1a1a;
  --grey:#777;
  --light-grey:#aaa;
  --rule:#222;
  --white:#fff;
  --dark-bg:#140905;
  --serif:'Tinos','Times New Roman',serif;
  --sans:'Open Sans',Arial,sans-serif;
}
*{margin:0;padding:0;box-sizing:border-box}
html,body{width:1200px;height:2927px;overflow:hidden}
body{font-family:var(--sans);color:var(--ink);background:var(--white);position:relative}
.wrap{position:relative;width:880px;margin:0 auto;height:100%}
a{color:inherit;text-decoration:none}

/* top bar */
.topbar{height:23px;background:var(--black)}
.topbar .links{position:absolute;left:0;top:6px;display:flex;gap:18px;font-size:9px;color:var(--white);text-transform:uppercase}
.topbar .social{position:absolute;right:0;top:3px;display:flex;gap:5px}
.topbar .social span{width:17px;height:17px;background:#3b6fb5;display:block}

/* header */
.header{height:110px}
.logo{position:absolute;left:0;top:22px;font-family:var(--serif);color:var(--ink);text-transform:uppercase;font-weight:400}
.logo .line1{font-size:35px;letter-spacing:2.5px;display:block;line-height:38px}
.logo .line2{font-size:22px;letter-spacing:3px;display:block;margin-left:148px;line-height:26px}
.search{position:absolute;left:544px;top:38px;width:160px;height:26px;border:1px solid #333;font-size:9px;padding:6px 6px}
.search svg{position:absolute;right:6px;top:6px}
.cart{position:absolute;left:718px;top:38px;width:162px;height:26px;background:var(--green);color:var(--white);font-size:9px;padding:7px 6px 0 30px}
.cart svg.bag{position:absolute;left:8px;top:6px}
.cart .drop{position:absolute;right:0;top:0;width:24px;height:26px;background:var(--green-dark)}
.cart .drop svg{position:absolute;left:7px;top:10px}

/* nav */
.nav{height:47px;background:var(--green);display:flex;justify-content:center;align-items:center;color:var(--white);font-size:12px;text-transform:uppercase}
.nav span.sep{margin:0 14px}

/* hero */
.hero{height:329px;position:relative;background:linear-gradient(90deg,#120905 0%,#2a1a10 40%,#5a4a3a 75%,#3a2a1c 100%)}
.hero .visual{position:absolute;left:330px;top:0;width:870px;height:329px;background:linear-gradient(100deg,rgba(0,0,0,0) 0%,rgba(120,150,40,.35) 30%,rgba(110,20,20,.35) 55%,rgba(220,180,60,.35) 80%,rgba(150,90,40,.3) 100%)}
.hero h1{position:absolute;left:0;top:60px;font-family:var(--serif);font-weight:400;font-size:40px;color:var(--green);text-transform:uppercase;letter-spacing:1px}
.hero p{position:absolute;left:0;top:122px;font-size:11px;color:var(--white)}
.btn{display:inline-block;background:var(--green);color:var(--white);font-family:var(--serif);font-weight:700;font-size:12px;text-transform:uppercase;text-align:center;letter-spacing:.5px}
.hero .btn{position:absolute;left:0;top:165px;width:122px;height:34px;line-height:34px}
.hero .arrows{position:absolute;left:405px;top:253px;display:flex}
.hero .arrows span{width:26px;height:26px;display:flex;align-items:center;justify-content:center}
.hero .arrows .prev{background:var(--black)}
.hero .arrows .next{background:var(--green)}

/* welcome */
.welcome{height:365px;text-align:center}
.welcome h2{font-family:var(--serif);font-weight:400;font-size:42px;padding-top:30px;line-height:50px}
.welcome .lead{font-size:12px;margin-top:20px}
.welcome .body{width:760px;margin:22px auto 0;font-size:11px;line-height:25px}
.welcome .btn{margin-top:38px;width:122px;height:36px;line-height:36px}

/* quality */
.quality{height:453px;background:var(--dark-bg)}
.quality .visual{position:absolute;left:0;top:36px;width:410px;height:380px;background:radial-gradient(ellipse at 40% 45%,#a8711e 0%,#6b3a10 35%,#2a1206 70%,#140905 100%)}
.quality .text{position:absolute;left:427px;top:35px;width:453px;color:var(--white)}
.quality h2{font-family:var(--serif);font-weight:400;font-size:42px;line-height:48px;text-transform:uppercase}
.quality h3{font-family:var(--serif);font-weight:400;font-size:26px;margin-top:6px}
.quality p{font-size:11px;line-height:25px;margin-top:20px}
.quality p + p{margin-top:24px}
.quality .btn{position:absolute;left:427px;top:375px;width:122px;height:36px;line-height:36px}

/* news */
.news{height:652px;text-align:center}
.section-title{font-family:var(--serif);font-weight:400;font-size:42px;line-height:48px}
.news .section-title{padding-top:46px}
.news .sub{font-family:var(--serif);font-size:28px;color:var(--grey);margin-top:10px}
.card{position:absolute;top:185px;width:428px;height:382px;text-align:left;border-bottom:2px solid var(--rule)}
.card.left{left:0}
.card.right{left:451px}
.card .photo{height:140px}
.card.left .photo{background:linear-gradient(90deg,#c98a1c 0%,#8a1020 35%,#b42a30 60%,#d79a2a 100%)}
.card.right .photo{background:linear-gradient(90deg,#2a1608 0%,#8a5020 40%,#c07a3a 70%,#3a1e0c 100%)}
.card .date{position:absolute;left:30px;top:205px;width:60px;text-align:center}
.card .date b{display:block;font-size:32px;font-weight:700;line-height:36px}
.card .date small{display:block;font-size:9px;text-transform:uppercase;margin-top:4px}
.card h4{position:absolute;left:148px;top:170px;width:250px;font-size:15px;font-weight:400;line-height:23px}
.card p{position:absolute;left:148px;top:224px;width:270px;font-size:10px;line-height:22px}
.card .more{position:absolute;right:0;top:348px;font-family:var(--serif);font-weight:700;font-size:10px;text-transform:uppercase}

/* newsletter */
.newsletter{height:253px;text-align:center}
.newsletter .section-title{padding-top:16px}
.newsletter .sub{font-family:var(--serif);font-size:14px;color:var(--grey);margin-top:10px}
.newsletter .field{position:absolute;left:150px;top:140px;width:355px;height:50px;border:1px solid #ccc}
.newsletter .btn{position:absolute;left:570px;top:140px;width:158px;height:50px;line-height:50px;font-size:19px;font-weight:400;letter-spacing:1px}

/* testimonials */
.testimonials{height:529px;background:radial-gradient(ellipse at 30% 40%,#5a1a18 0%,#2a0e0a 45%,#150605 100%)}
.testimonials .photo{position:absolute;left:0;top:88px;width:376px;height:353px;background:linear-gradient(120deg,#2a3a80 0%,#b0305a 35%,#d8a070 60%,#5a2a6a 100%)}
.testimonials .panel{position:absolute;left:376px;top:88px;width:502px;height:353px;background:var(--green);color:var(--white);padding:40px 32px 0 32px}
.testimonials .panel::after{content:"";position:absolute;right:0;bottom:0;border-style:solid;border-width:0 0 22px 22px;border-color:transparent transparent #142f00 transparent;opacity:.55}
.testimonials h2{font-family:var(--serif);font-weight:400;font-size:44px;line-height:46px;text-transform:uppercase}
.testimonials p{font-size:11px;line-height:25px;margin-top:22px}

/* footer */
.footer{height:184px}
.footer .col{position:absolute;top:40px;width:140px}
.footer h5{font-size:10px;font-weight:700;color:var(--green);text-transform:uppercase;margin-bottom:6px}
.footer li{list-style:none;font-size:10px;line-height:20px;color:var(--light-grey);text-transform:uppercase}
.footer .totop{position:absolute;left:910px;top:132px;width:34px;height:34px;background:var(--green);display:flex;align-items:center;justify-content:center}
.copyright{height:35px;background:var(--green);color:var(--white);font-size:10px;text-align:center;line-height:35px}
</style>
</head>
<body>

<div class="topbar">
  <div class="wrap">
    <nav class="links"><a>Home</a><a>Wish List (0)</a><a>My Account</a><a>Shopping Cart</a><a>Checkout</a><a>Login</a><a>Create an Account</a></nav>
    <div class="social" aria-label="Social links"><span></span><span></span><span></span><span></span></div>
  </div>
</div>

<header class="header">
  <div class="wrap">
    <div class="logo"><span class="line1">Brackenford Lane</span><span class="line2">Vineyard</span></div>
    <div class="search">SEARCH...
      <svg width="12" height="12" viewBox="0 0 12 12"><circle cx="5" cy="5" r="3.8" fill="none" stroke="#222" stroke-width="1.5"/><line x1="7.8" y1="7.8" x2="11" y2="11" stroke="#222" stroke-width="1.6"/></svg>
    </div>
    <div class="cart">
      <svg class="bag" width="14" height="13" viewBox="0 0 14 13"><path d="M0 1h3l2 7h7l2-5H4" fill="none" stroke="#fff" stroke-width="1.4"/><circle cx="6" cy="11" r="1.3" fill="#fff"/><circle cx="11" cy="11" r="1.3" fill="#fff"/></svg>
      Cart: 0 item(s) - $0.00
      <span class="drop"><svg width="10" height="6" viewBox="0 0 10 6"><path d="M0 0h10L5 6z" fill="#fff"/></svg></span>
    </div>
  </div>
</header>

<nav class="nav">
  <a>Home</a><span class="sep">|</span><a>Wine</a><span class="sep">|</span><a>Contact Us</a><span class="sep">|</span><a>Events</a><span class="sep">|</span><a>Gallery</a><span class="sep">|</span><a>About Us</a><span class="sep">|</span><a>Cart</a><span class="sep">|</span><a>Members</a><span class="sep">|</span><a>Outlets</a>
</nav>

<section class="hero">
  <div class="visual" role="img" aria-label="Glass of red wine, bottle, grapes, cheese and bread on a rustic table"></div>
  <div class="wrap">
    <h1>Brackenford Lane</h1>
    <p>Everything is lovingly handpicked and made locally to produce high quality wine.</p>
    <a class="btn">Learn More</a>
    <div class="arrows">
      <span class="prev"><svg width="8" height="10" viewBox="0 0 8 10"><path d="M6 0L1 5l5 5" fill="none" stroke="#fff" stroke-width="1.8"/></svg></span>
      <span class="next"><svg width="8" height="10" viewBox="0 0 8 10"><path d="M2 0l5 5-5 5" fill="none" stroke="#fff" stroke-width="1.8"/></svg></span>
    </div>
  </div>
</section>

<section class="welcome">
  <h2>WELCOME!</h2>
  <p class="lead">Great Tasting Wine with a Splash of Fruit Just what you've been lookig for</p>
  <p class="body">Lorem Ipsum is simply dummy text of the printing and typesetting industry. Lorem Ipsum has been the industry's standard dummy text ever since the 1500s, when an unknown printer took a galley of type and scrambled it to make a type specimen book. It has survived not only five centuries, but also the leap into electronic typesetting, remaining essentially unchanged. It was popularised in the 1960s with the release of Presstype sheets containing Lorem Ipsum passages, and more recently with desktop publishing software like Inkwell Layout including versions of Lorem Ipsum.</p>
  <a class="btn">Learn More</a>
</section>

<section class="quality">
  <div class="wrap">
    <div class="visual" role="img" aria-label="Candle, glass of white wine, bottle and green grapes in warm light"></div>
    <div class="text">
      <h2>Perfect Quality</h2>
      <h3>Luytas letytuyse deluiuyas</h3>
      <p>Lorem Ipsum is simply dummy text of the printing<br>Lorem Ipsum has been the industry's standard dummy text ever since the 1500s, when an unknown printer took a galley of type and scrambled it to make a type specimen book.</p>
      <p>It has survived not only five centuries, but also the leap into electronic typesetting, remaining essentially unchanged. It was popularised in the 1960s with the release of Presstype sheets containing.</p>
    </div>
    <a class="btn">Learn More</a>
  </div>
</section>

<section class="news">
  <div class="wrap">
    <h2 class="section-title">NEWS &amp; EVENTS</h2>
    <p class="sub">msequi nesciunt neque porro quis neuamesa</p>
    <article class="card left">
      <div class="photo" role="img" aria-label="Close-up of red grapes"></div>
      <div class="date"><b>15</b><small>March</small></div>
      <h4>Serertas erta mioras deloreas fertasetase</h4>
      <p>Lorem Ipsum is simply dummy text of the printing and typesetting industry. Lorem Ipsum has been the industry's standard dummy text ever since the 1500s.</p>
      <a class="more">Read More</a>
    </article>
    <article class="card right">
      <div class="photo" role="img" aria-label="Row of oak wine barrels in a cellar"></div>
      <div class="date"><b>13</b><small>April</small></div>
      <h4>Serertas erta mioras deloreas fertasetase</h4>
      <p>Lorem Ipsum is simply dummy text of the printing and typesetting industry. Lorem Ipsum has been the industry's standard dummy text ever since the 1500s.</p>
      <a class="more">Read More</a>
    </article>
  </div>
</section>

<section class="newsletter">
  <div class="wrap">
    <h2 class="section-title">NEWSLETTER SIGN UP</h2>
    <p class="sub">Lorem Ipsum is simply dummy text of the printing and typesetting industry. Lorem Ipsum has</p>
    <div class="field"></div>
    <a class="btn">Subscribe</a>
  </div>
</section>

<section class="testimonials">
  <div class="wrap">
    <div class="photo" role="img" aria-label="Group of friends raising wine glasses at a party"></div>
    <div class="panel">
      <h2>What<br>People are saying</h2>
      <p>Lorem Ipsum is simply dummy text of the printing and typesetting industry. Lorem Ipsum has been the industry's standard dummy text ever since the 1500s, when an unknown printer took a galley of type and scrambled it to make a type specimen book. It has survived not only five centuries, when an unknown printer took a galley of type and scrambled it to make a type specimen book. It has survived not only five centuries.</p>
    </div>
  </div>
</section>

<footer class="footer">
  <div class="wrap">
    <div class="col" style="left:0"><h5>Information</h5><ul><li>About Us</li><li>Delivery</li><li>Privacy Policy</li><li>Terms &amp; Conditions</li></ul></div>
    <div class="col" style="left:150px"><h5>Customer Service</h5><ul><li>Contact Us</li><li>Returns</li><li>Site Map</li></ul></div>
    <div class="col" style="left:300px"><h5>Extras</h5><ul><li>Brands</li><li>Gift Vouchers</li><li>Affiliates</li><li>Specials</li></ul></div>
    <div class="col" style="left:450px"><h5>My Account</h5><ul><li>My Account</li><li>Order History</li><li>Wish List</li><li>Newsletter</li></ul></div>
    <div class="col" style="left:600px"><h5>Follow Us</h5><ul><li>Grapevine Social</li><li>Cellar Notes</li><li>RSS</li><li>Vineyard TV</li></ul></div>
    <div class="col" style="left:750px"><h5>Online Support</h5><ul><li>+61 400 318 562</li><li>1-800-472-9031</li></ul></div>
    <a class="totop" aria-label="Back to top"><svg width="12" height="8" viewBox="0 0 12 8"><path d="M1 7l5-5 5 5" fill="none" stroke="#fff" stroke-width="2"/></svg></a>
  </div>
</footer>
<div class="copyright">Copyright © 2016 Brackenford Lane Vineyard</div>

</body>
</html>
```